Maple Crest Glow Skin Studio needs an 8 page WP redesign

We need a colorful re-design for an 8 page Wordpress website. The current preliminary website is live. The home page URL is http://maplecrestglowskinstudio.example The new logo is live on the website also. I would like a (re)design using the colors that are represented by the new logo file, and any additional complimentary colors. The information regarding the business can be found on the website already, so please review it for insight. The name of the business is "Maple Crest Glow Skin Studio".

Target Market(s)

The targeted website viewer is an adult female between the ages of 30 and 75 who is interested in facial renewal, wart removal and scar removal. This website should inspire in the target viewer the benefits of laser facial renewal, wart removal and new scar removal. Potential website viewers are wanting and searching for improved skin health and appearance. The website must represent the essence of a professional spa business.

Industry/Entity Type

Business

Font styles to use
Sans Serif

Requirements
Must have
• - The phone number placed in a visible and high value widget area that allows mobile phone browser dialing.

```html
<!DOCTYPE html>
<html lang="en">
<head>
<meta charset="utf-8">
<title>Maple Crest Glow Skin Studio</title>
<link href="https://fonts.googleapis.com/css2?family=Roboto:wght@300;400;500&family=Arimo:wght@400;700&display=swap" rel="stylesheet">
<style>
  :root {
    --plum: #4a1d45;
    --plum-deep: #3f173b;
    --magenta: #b0249b;
    --phone: #c41eb0;
    --ink: #333333;
    --muted: #6b6b6b;
    --rule: #cfcfcf;
    --panel: #f6f6f6;
    --white: #ffffff;
  }
  * { box-sizing: border-box; margin: 0; padding: 0; }
  html, body { width: 1200px; height: 1075px; overflow: hidden; background: var(--white); }
  body { position: relative; font-family: "Arimo", Arial, sans-serif; color: var(--ink); }
  a { color: inherit; text-decoration: none; }

  .site-header { position: absolute; left: 0; top: 0; width: 1200px; height: 87px; border-bottom: 1px solid var(--rule); }
  .brand { position: absolute; left: 269px; top: 26px; display: flex; align-items: center; gap: 9px; }
  .brand-dot { width: 14px; height: 14px; border-radius: 50%; background: var(--magenta); }
  .brand-name { font-family: "Roboto", sans-serif; font-weight: 500; font-size: 19px; color: var(--plum); line-height: 1.15; width: 170px; }
  .contact { position: absolute; right: 283px; top: 24px; text-align: right; }
  .contact-address { font-size: 7.5px; color: var(--ink); }
  .contact-phone { display: flex; align-items: center; gap: 8px; margin-top: 11px; font-family: "Roboto", sans-serif; font-size: 14.5px; color: var(--phone); }

  .main-nav { position: absolute; left: 0; top: 87px; width: 1200px; height: 30px; border-bottom: 2px solid var(--rule); }
  .main-nav ul { list-style: none; position: absolute; left: 269px; top: 0; display: flex; height: 28px; }
  .main-nav li { font-size: 8.5px; font-weight: 700; color: #444; height: 28px; line-height: 28px; padding: 0 17px; }
  .main-nav li.is-current { background: var(--plum); color: var(--white); padding: 0 19px 0 19px; }
  .main-nav li:nth-child(3), .main-nav li:nth-child(4), .main-nav li:nth-child(5) { padding: 0 22px; }
  .nav-search { position: absolute; left: 892px; top: 4px; height: 20px; border-left: 1px solid var(--rule); padding-left: 10px; }

  .hero { position: absolute; left: 0; top: 117px; width: 1200px; height: 342px; background: #fcfcfc; border-bottom: 1px solid var(--rule); overflow: hidden; }
  .hero-photo { position: absolute; left: 527px; top: 0; width: 580px; height: 342px;
    background: radial-gradient(ellipse at 55% 40%, #ecd2c2 0%, #e4c2ad 30%, #f2ece8 60%, #fafafa 85%); }
  .hero-title { position: absolute; left: 268px; top: 123px; font-family: "Roboto", sans-serif; font-weight: 400; font-size: 29px; color: var(--plum); }
  .hero-sub { position: absolute; left: 268px; top: 161px; font-family: "Roboto", sans-serif; font-size: 14.5px; color: var(--plum); }
  .hero-dots { position: absolute; left: 577px; top: 307px; display: flex; gap: 2px; }
  .hero-dots span { width: 8px; height: 8px; border-radius: 50%; background: var(--plum); }
  .hero-dots span.is-active { background: var(--magenta); }

  .intro { position: absolute; left: 0; top: 459px; width: 1200px; height: 329px; background: var(--panel); }
  .announce { position: absolute; left: 269px; top: 0; width: 142px; height: 30px; background: var(--magenta); color: var(--white);
    font-size: 7.5px; display: flex; align-items: center; justify-content: space-between; padding: 0 10px 0 14px; }
  .intro-photo { position: absolute; left: 269px; top: 62px; width: 236px; height: 267px;
    background: radial-gradient(ellipse at 55% 40%, #e9c4ad 0%, #d9a98c 35%, #efe2d9 70%, var(--panel) 95%); border-radius: 45% 45% 0 0; }
  .intro-copy { position: absolute; left: 561px; top: 80px; width: 356px; }
  .intro-copy h2 { font-family: "Roboto", sans-serif; font-weight: 300; font-size: 15.5px; color: var(--plum); margin-bottom: 16px; }
  .intro-copy p { font-size: 8px; line-height: 12.2px; color: var(--muted); margin-bottom: 10px; }

  .recent { position: absolute; left: 0; top: 788px; width: 1200px; height: 127px; background: var(--plum); }
  .recent-tab { position: absolute; left: 269px; top: 0; width: 98px; height: 30px; background: var(--magenta); color: var(--white);
    font-size: 10px; line-height: 30px; text-align: center; }
  .post { position: absolute; top: 46px; display: flex; gap: 18px; color: var(--white); }
  .post-date { text-align: center; font-family: "Roboto", sans-serif; }
  .post-day { font-size: 26px; font-weight: 300; line-height: 1; }
  .post-month { font-size: 12px; line-height: 1.1; }
  .post-title { font-size: 8.5px; line-height: 12px; width: 100px; margin-top: 6px; }
  .post-divider { position: absolute; top: 52px; width: 1px; height: 42px; background: #6a3f64; }

  .site-footer { position: absolute; left: 0; top: 915px; width: 1200px; height: 160px; }
  .footer-brand { position: absolute; left: 269px; top: 22px; display: flex; align-items: center; gap: 8px; }
  .footer-brand .brand-name { font-size: 14px; width: 120px; }
  .footer-brand .brand-dot { width: 11px; height: 11px; }
  .copyright { position: absolute; left: 269px; top: 66px; font-size: 7.5px; color: var(--ink); }
  .footer-col { position: absolute; top: 20px; }
  .footer-col h3 { font-family: "Roboto", sans-serif; font-weight: 400; font-size: 11px; color: #444; margin-bottom: 13px; }
  .footer-col ul { list-style: none; }
  .footer-col li { font-size: 7.5px; color: var(--muted); line-height: 14px; }
  .footer-col li.is-current { color: var(--plum); text-decoration: underline; }
  .social { display: flex; gap: 10px; }
  .social span { width: 21px; height: 21px; border-radius: 50%; background: #8a8a8a; }
  .social span:first-child { background: var(--plum); }
</style>
</head>
<body>
  <header class="site-header">
    <a class="brand" href="#"><span class="brand-dot"></span><span class="brand-name">Maple Crest Glow Skin Studio</span></a>
    <div class="contact">
      <p class="contact-address">2480 Birchwood Ave, Suite 210, Maple Crest, TX 75012</p>
      <a class="contact-phone" href="tel:5550184420">
        <svg width="16" height="16" viewBox="0 0 16 16" aria-hidden="true"><circle cx="8" cy="8" r="7" fill="none" stroke="#c41eb0" stroke-width="1.3"/><path d="M5.3 5.2c.5 2.5 2.6 4.8 5.3 5.5l.9-1.3-1.6-.9-.7.6c-1-.5-1.7-1.3-2.1-2.2l.6-.7-.8-1.6z" fill="#c41eb0"/></svg>
        Phone: (555) 018-4420
      </a>
    </div>
  </header>

  <nav class="main-nav">
    <ul>
      <li class="is-current">Home</li>
      <li>About Us</li>
      <li>Skin Renewal</li>
      <li>Scar Removal</li>
      <li>Wart Removal</li>
      <li>Blog</li>
      <li>Contact Us</li>
    </ul>
    <div class="nav-search">
      <svg width="16" height="16" viewBox="0 0 16 16" aria-hidden="true"><circle cx="6" cy="6" r="4.3" fill="none" stroke="#888" stroke-width="1.6"/><path d="M9.3 9.3l5 5" stroke="#888" stroke-width="2.2" stroke-linecap="round"/></svg>
    </div>
  </nav>

  <section class="hero">
    <div class="hero-photo" role="img" aria-label="Photo of a relaxed woman in a white towel wrap holding a white calla lily"></div>
    <h1 class="hero-title">Laser Skin Renewal</h1>
    <p class="hero-sub">No Downtime, Minimal Discomfort, No Disposables</p>
    <div class="hero-dots"><span class="is-active"></span><span></span><span></span></div>
  </section>

  <section class="intro">
    <div class="announce"><span>SPECIAL ANNOUNCEMENT</span>
      <svg width="10" height="6" viewBox="0 0 10 6" aria-hidden="true"><path d="M1 1l4 4 4-4" fill="none" stroke="#fff" stroke-width="1"/></svg>
    </div>
    <div class="intro-photo" role="img" aria-label="Photo of a smiling woman with a pink orchid in her hair"></div>
    <div class="intro-copy">
      <h2>Have you considered Laser Skin Renewal Therapy?</h2>
      <p>You will truly love laser skin renewal if your skin is showing signs of premature aging or the skin has sustained sun damage. Conditions such as excessive redness due to sun exposure or fine lines will be concerns of the past. In fact, laser skin therapy is a unique and innovative way to enjoy youthful and healthy skin without resorting to painful and inconvenient surgery.</p>
      <p>Both men and women are receiving benefits from laser skin therapy.</p>
      <p>The literature contains ample scientific evidence to support laser skin renewal. After this therapy, your skin will produce collagen, which reduces and minimizes the appearance of fine lines and wrinkles. Imagine getting all this with minimal pain and no downtime? Doesn't it make you feel like getting in touch with our laser skin specialist today?</p>
    </div>
  </section>

  <section class="recent">
    <div class="recent-tab">RECENT POSTS</div>
    <article class="post" style="left:268px"><div class="post-date"><div class="post-day">12</div><div class="post-month">DEC</div></div><p class="post-title">The Benefits of Laser Skin Rejuvenation</p></article>
    <span class="post-divider" style="left:457px"></span>
    <article class="post" style="left:503px"><div class="post-date"><div class="post-day">14</div><div class="post-month">DEC</div></div><p class="post-title">The Benefits of Laser Skin Rejuvenation</p></article>
    <span class="post-divider" style="left:695px"></span>
    <article class="post" style="left:750px"><div class="post-date"><div class="post-day">16</div><div class="post-month">DEC</div></div><p class="post-title">The Benefits of Laser Skin Rejuvenation</p></article>
  </section>

  <footer class="site-footer">
    <div class="footer-brand"><span class="brand-dot"></span><span class="brand-name">Maple Crest Glow Skin Studio</span></div>
    <p class="copyright">© 2015 • Privacy Policy</p>
    <div class="footer-col" style="left:460px">
      <h3>INFORMATION</h3>
      <ul><li>Home</li><li>About Us</li><li class="is-current">Skin Renewal</li><li>Scar Removal</li><li>Wart Removal</li><li>Blog</li><li>Contact Us</li></ul>
    </div>
    <div class="footer-col" style="left:601px">
      <h3>META</h3>
      <ul><li>Log in</li><li>Entries RSS</li><li>Comments RSS</li><li>SitePress.example</li></ul>
    </div>
    <div class="footer-col" style="left:725px">
      <h3>SOCIAL LINKS</h3>
      <div class="social"><span></span><span></span><span></span></div>
    </div>
  </footer>
</body>
</html>
```